Medical Company in need of Modern business card design for new Wound Care clinic.

Modern business card design for our Woundcare company. Logo and description of services can be found on our website; https://www.tovrel-woundcare.com/

```html
<!DOCTYPE html>
<html lang="en">
<head>
<meta charset="utf-8">
<title>Tovrel Woundcare — Business Card</title>
<link href="https://fonts.googleapis.com/css2?family=Montserrat:wght@500&family=Open+Sans:wght@400;700&display=swap" rel="stylesheet">
<style>
  :root {
    --backdrop: #3a3a3a;
    --card-white: #ffffff;
    --card-black: #141414;
    --gold: #f0bc5e;
    --gold-deep: #c8923a;
    --ink: #111111;
  }
  * { margin: 0; padding: 0; box-sizing: border-box; }
  html, body { width: 1200px; height: 689px; overflow: hidden; }
  body {
    background: var(--backdrop);
    font-family: "Open Sans", Arial, sans-serif;
    position: relative;
  }
  .card {
    position: absolute;
    top: 190px;
    width: 540px;
    height: 309px;
    border-radius: 18px;
    overflow: hidden;
    background: var(--card-white);
    box-shadow: 0 18px 40px rgba(0,0,0,.45);
  }
  .card--front { left: 40px; }
  .card--back { left: 620px; }

  .wordmark {
    font-family: "Montserrat", Arial, sans-serif;
    font-weight: 500;
    letter-spacing: .32em;
    text-transform: uppercase;
    display: flex;
    align-items: center;
    gap: 14px;
  }
  .wordmark__mark {
    width: 22px; height: 22px;
    background: var(--gold-deep);
  }
  .card--front .wordmark {
    position: absolute;
    inset: 0;
    justify-content: center;
    font-size: 30px;
    color: var(--ink);
  }

  .back-art { position: absolute; inset: 0; width: 100%; height: 100%; }
  .card--back .wordmark {
    position: absolute;
    top: 46px; right: 52px;
    font-size: 17px;
    color: var(--gold);
    letter-spacing: .28em;
  }
  .card--back .wordmark__mark { width: 14px; height: 14px; background: var(--gold); }

  .person {
    position: absolute;
    left: 52px; top: 186px;
    padding-left: 14px;
    border-left: 6px solid var(--gold);
  }
  .person__name {
    font-weight: 700; font-size: 19px; color: var(--gold);
    text-transform: uppercase; line-height: 1.1;
  }
  .person__role { font-size: 12px; color: var(--ink); }

  .contacts {
    position: absolute; left: 72px; top: 236px;
    list-style: none; font-size: 11px; color: var(--ink); line-height: 15px;
  }
  .contacts li { display: flex; align-items: center; gap: 6px; }
  .contacts svg { width: 10px; height: 10px; flex: none; }

  .addresses {
    position: absolute; right: 30px; top: 196px;
    text-align: right; font-size: 11.5px; color: var(--ink); line-height: 16px;
  }
  .addresses p + p { margin-top: 10px; }
</style>
</head>
<body>

<section class="card card--front">
  <div class="wordmark"><span class="wordmark__mark"></span>Tovrel Woundcare</div>
</section>

<section class="card card--back">
  <svg class="back-art" viewBox="0 0 540 309" preserveAspectRatio="none" aria-hidden="true">
    <defs>
      <linearGradient id="goldSweep" x1="0" y1="1" x2="1" y2="0">
        <stop offset="0" stop-color="#e0a94a"/>
        <stop offset=".6" stop-color="#f5c56a"/>
        <stop offset="1" stop-color="#f0bc5e"/>
      </linearGradient>
    </defs>
    <path d="M0 196 C90 150 190 150 300 140 C420 130 500 100 540 30 L540 48 C505 120 430 150 300 158 C190 166 90 176 0 224 Z" fill="url(#goldSweep)"/>
    <path d="M0 0 H540 V30 C500 100 420 128 300 136 C190 144 90 146 0 190 Z" fill="var(--card-black)"/>
  </svg>

  <div class="wordmark"><span class="wordmark__mark"></span>Tovrel Woundcare</div>

  <div class="person">
    <p class="person__name">Daniel Reyes</p>
    <p class="person__role">Managing Director</p>
  </div>

  <ul class="contacts">
    <li><svg viewBox="0 0 10 10"><circle cx="5" cy="5" r="5" fill="var(--gold)"/><path d="M3 2.5 L4 4.5 L3.6 5 Q4.5 6.5 5.5 6.8 L6 6.2 L7.6 7.2 L7 8 Q3 7.5 2.3 3 Z" fill="#fff"/></svg>555-014-2868</li>
    <li><svg viewBox="0 0 10 10"><rect x="1.5" y="2" width="7" height="6.5" rx="1" fill="var(--gold)"/><rect x="3" y="3.5" width="4" height="1.5" fill="#fff"/></svg>555-014-2867</li>
    <li><svg viewBox="0 0 10 10"><rect x="1" y="2.5" width="8" height="5.5" fill="var(--gold)"/><path d="M1 2.5 L5 5.6 L9 2.5" fill="none" stroke="#fff" stroke-width=".8"/></svg>info@tovrelmail.com</li>
    <li><svg viewBox="0 0 10 10"><circle cx="5" cy="5" r="4.5" fill="var(--gold)"/><path d="M0.5 5 H9.5 M5 .5 Q2.5 5 5 9.5 M5 .5 Q7.5 5 5 9.5" fill="none" stroke="#fff" stroke-width=".6"/></svg>www.tovrel-woundcare.com</li>
  </ul>

  <div class="addresses">
    <p>4410 Birchwood Lane Bldg. C, suite 118</p>
    <p>2186 Harlow Rd Ste 100 PMB<br>512087 Springvale, TX 75001</p>
  </div>
</section>

</body>
</html>
```